Business Card design for Brightvale Global

we need a business card design for our company. we are a trading company based in LA.

Company Name: Brightvale Global Corp.
Contact: Marla Ostrov
Title: CEO
Tel: 310-447-2093
Email: bvgcorp7@mailnest.example

Target Market(s)

International, especially China

Industry/Entity Type

Trade

Colors
3276b5
34a7d8
0555a3
0493ce
85cae6
85acd3
d0dfed
cee9f5

Requirements
Must have
• Logo and contact, to have international/global feeling

```html
<!DOCTYPE html>
<html lang="en">
<head>
<meta charset="UTF-8">
<title>Brightvale Global — Business Card</title>
<link rel="stylesheet" href="https://fonts.googleapis.com/css2?family=Lato:wght@400;700&family=Montserrat:wght@600;700&display=swap">
<style>
  :root {
    --backdrop: #1e1e1e;
    --navy: #143a6b;
    --navy-deep: #0f2f5a;
    --brand-blue: #0493ce;
    --accent-blue: #3276b5;
    --ink: #3a3f47;
    --paper: #ffffff;
    --pale: #d0dfed;
    --pale-sky: #cee9f5;
  }
  * { margin: 0; padding: 0; box-sizing: border-box; }
  html, body {
    width: 1200px;
    height: 900px;
    overflow: hidden;
    background: var(--backdrop);
  }
  .canvas {
    position: relative;
    width: 1200px;
    height: 900px;
  }
  .card {
    position: absolute;
    left: 320px;
    width: 560px;
    height: 320px;
    border-radius: 22px;
    overflow: hidden;
    box-shadow: 0 14px 30px rgba(0,0,0,0.45);
  }
  .card--back {
    top: 100px;
    background: var(--navy);
  }
  .card--front {
    top: 480px;
    background: var(--paper);
  }
  .world-map-area {
    position: absolute;
    inset: 30px 40px;
    border-radius: 40px;
    background: radial-gradient(ellipse at center, rgba(133,172,211,0.16), rgba(133,172,211,0.02) 70%);
  }
  .brand {
    font-family: "Montserrat", sans-serif;
    font-weight: 700;
    display: flex;
    align-items: center;
    gap: 12px;
  }
  .brand__dot {
    width: 34px;
    height: 34px;
    border-radius: 50%;
  }
  .card--back .brand {
    position: absolute;
    left: 50%;
    top: 50%;
    transform: translate(-50%, -50%);
    font-size: 36px;
    color: var(--paper);
    white-space: nowrap;
  }
  .card--back .brand__dot { background: var(--paper); }
  .card--front .brand {
    position: absolute;
    left: 40px;
    top: 42px;
    font-size: 30px;
    color: var(--navy);
  }
  .card--front .brand__dot { background: var(--brand-blue); width: 30px; height: 30px; }
  .faint-circle {
    position: absolute;
    right: -80px;
    top: -10px;
    width: 300px;
    height: 300px;
    border-radius: 50%;
    border: 26px solid var(--pale);
    opacity: 0.55;
  }
  .contact-name {
    position: absolute;
    left: 52px;
    top: 168px;
    font-family: "Montserrat", sans-serif;
    font-weight: 700;
    font-size: 19px;
    letter-spacing: 0.3px;
    text-transform: uppercase;
  }
  .contact-name__first { color: var(--accent-blue); }
  .contact-name__last { color: var(--navy); }
  .contact-title {
    position: absolute;
    left: 52px;
    top: 194px;
    font-family: "Lato", sans-serif;
    font-size: 15px;
    color: var(--ink);
  }
  .contact-list {
    position: absolute;
    left: 52px;
    top: 238px;
    list-style: none;
    font-family: "Lato", sans-serif;
    font-size: 16px;
    color: var(--ink);
  }
  .contact-list li {
    display: flex;
    align-items: center;
    gap: 6px;
    margin-bottom: 4px;
  }
  .contact-icon { width: 18px; height: 18px; flex: none; }
</style>
</head>
<body>
<main class="canvas">
  <section class="card card--back" aria-label="Card back">
    <div class="world-map-area" role="img" aria-label="Faint dotted world map pattern"></div>
    <div class="brand"><span class="brand__dot"></span>Brightvale Global</div>
  </section>

  <section class="card card--front" aria-label="Card front">
    <div class="faint-circle" aria-hidden="true"></div>
    <div class="brand"><span class="brand__dot"></span>Brightvale Global</div>
    <p class="contact-name"><span class="contact-name__first">Marla</span> <span class="contact-name__last">Ostrov</span></p>
    <p class="contact-title">CEO</p>
    <ul class="contact-list">
      <li>
        <svg class="contact-icon" viewBox="0 0 20 20" aria-hidden="true">
          <circle cx="10" cy="10" r="10" fill="#0493ce"/>
          <path d="M5 8.2c0-1.2 2.2-2.4 5-2.4s5 1.2 5 2.4l-1.6.8-1-1.4H7.6l-1 1.4z M6.5 14.5l1.2-4h4.6l1.2 4z" fill="#fff"/>
        </svg>
        310-447-2093
      </li>
      <li>
        <svg class="contact-icon" viewBox="0 0 20 20" aria-hidden="true">
          <circle cx="10" cy="10" r="10" fill="#0493ce"/>
          <rect x="5" y="6.5" width="10" height="7" rx="1" fill="#fff"/>
          <path d="M5.3 7l4.7 3.6L14.7 7" fill="none" stroke="#0493ce" stroke-width="1"/>
        </svg>
        bvgcorp7@mailnest.example
      </li>
    </ul>
  </section>
</main>
</body>
</html>
```